Home Staging Company needs business card design

We're a home staging company called Brightly Settled Home Staging. We would like a business card design that includes aqua and gray. Our current logo of house within chair is fine but I find we almost always use the logo in one color. I'll upload images of front and back of our current card and our logo. Note that we have dropped "Solutions" from our company name and don't want to include it on the card.

Target Market(s)

Realtors and homeowners - people interested in selling their homes

Contact Information for Business Card

Marisol Vantrease
Brightly Settled Home Staging
612-348-9071
www.brightlysettled.example
marisol@brightlysettled.example

Font styles to use
Serif
Script

Requirements
Must have
• My logo and contact details
• UPDATE***
• I forgot to say that the company name should be included on the front of the card somehow.

```html
<!DOCTYPE html>
<html lang="en">
<head>
<meta charset="utf-8">
<title>Brightly Settled Home Staging – Business Card</title>
<link rel="stylesheet" href="https://fonts.googleapis.com/css2?family=Lora:wght@400;600&family=Roboto:wght@300;400&display=swap">
<style>
  :root {
    --aqua: #4fc6c3;
    --blue: #1a8fd6;
    --gray-light: #dcdcdc;
    --gray-text: #4a4a4a;
    --paper: #f7f7f7;
    --backdrop: #3b3d3f;
    --white: #ffffff;
  }
  * { box-sizing: border-box; margin: 0; padding: 0; }
  html, body { width: 1200px; height: 786px; overflow: hidden; }
  body {
    background: var(--backdrop);
    display: flex;
    align-items: center;
    justify-content: center;
    gap: 60px;
    font-family: "Roboto", Arial, sans-serif;
  }
  .card {
    position: relative;
    width: 500px;
    height: 286px;
    border-radius: 16px;
    overflow: hidden;
    box-shadow: 0 10px 26px rgba(0,0,0,0.35);
  }
  .card-front { background: var(--paper); }
  .card-back {
    background: var(--aqua);
    display: flex;
    flex-direction: column;
    align-items: center;
    justify-content: center;
    gap: 22px;
  }
  .wave { position: absolute; inset: 0; width: 100%; height: 100%; }
  .wordmark {
    font-family: "Lora", Georgia, serif;
    font-weight: 600;
    line-height: 1.05;
    display: flex;
    align-items: center;
    gap: 12px;
  }
  .wordmark-dot {
    width: 30px; height: 30px; border-radius: 50%;
    flex-shrink: 0;
  }
  .wordmark-name { font-size: 30px; }
  .wordmark-sub {
    display: block;
    font-size: 12px;
    letter-spacing: 0.42em;
    text-transform: uppercase;
    margin-top: 6px;
  }
  .card-front .wordmark {
    position: absolute; top: 36px; right: 40px;
    color: var(--gray-text);
  }
  .card-front .wordmark-dot { background: var(--gray-text); }
  .card-back .wordmark { color: var(--white); }
  .card-back .wordmark-dot { background: var(--white); }
  .person-name {
    position: absolute; left: 36px; top: 160px;
    font-family: "Lora", Georgia, serif;
    font-size: 19px;
    letter-spacing: 0.06em;
    line-height: 1.25;
    text-transform: uppercase;
    color: var(--white);
  }
  .contact {
    position: absolute; right: 180px; bottom: 14px;
    text-align: right;
    font-size: 13px;
    font-weight: 300;
    line-height: 1.45;
    color: var(--white);
  }
  .web {
    font-size: 13px;
    font-weight: 300;
    color: var(--white);
    letter-spacing: 0.02em;
  }
</style>
</head>
<body>
  <section class="card card-front" aria-label="Business card front">
    <svg class="wave" viewBox="0 0 500 286" preserveAspectRatio="none" aria-hidden="true">
      <path d="M0,96 C150,100 260,160 340,205 C400,240 450,254 500,254 L500,286 L0,286 Z" fill="var(--gray-light)"/>
      <path d="M0,103 C150,107 258,168 336,213 C398,248 450,262 500,262 L500,286 L0,286 Z" fill="var(--blue)"/>
      <path d="M0,112 C150,116 254,178 330,222 C394,258 448,272 500,272 L500,286 L0,286 Z" fill="var(--aqua)"/>
    </svg>
    <div class="wordmark">
      <span class="wordmark-dot"></span>
      <span><span class="wordmark-name">Brightly Settled</span><span class="wordmark-sub">Home Staging</span></span>
    </div>
    <p class="person-name">Marisol<br>Vantrease</p>
    <p class="contact">612-348-9071<br>marisol@brightlysettled.example</p>
  </section>

  <section class="card card-back" aria-label="Business card back">
    <div class="wordmark">
      <span class="wordmark-dot"></span>
      <span><span class="wordmark-name">Brightly Settled</span><span class="wordmark-sub">Home Staging</span></span>
    </div>
    <p class="web">www.brightlysettled.example</p>
  </section>
</body>
</html>
```